Business Card for Polygraph business in Africa

Business Card . Polygraph Examiner based in Tanzania, East Africa.
Business Card will be used to disseminate contact information to potential clients.
It should convey that I am a professional specifically in the polygraph field and perform my work with integrity.

I have attached the business card that I'm currently using, which I threw together myself initially. It's not professional enough.

Target Market(s)

Banks, Accounting Firms, Government Ministries, Gas, Oil, & Gemstone Mining Concerns, Wildlife Conservation NGOs, International companies located in East Africa.

Industry/Entity Type

Business

Contact Information for Business Card

Veritas Lumeno
Harriet Munsell
PO Box 48317
Arusha, Tanzania
+255 712 839 254
harrietmunsell@quillpost.example

Colors
00a990
f37122
faa54b

Requirements
Must have
• - Veritas Lumeno (with the word "Polygraph" being more prominent than the word "Tanzania")
• - Forensic Examinations
• - Employment Screening
• - Should contain a logo of the Continental Truthfinder Guild (of which I'm a member)
• - I would like an accent design (such as the polygraph "squiggles" of a cardio tracing or such as that)
• - My contact information (less prominent, but large enough to read legibly). I would also consider putting the contact information on the second side of the card.
Nice to have
• My color suggestions are changeable.
Should not have
• Anything "cutesy" or "cartoonish"

```html
<!DOCTYPE html>
<html lang="en">
<head>
<meta charset="utf-8">
<title>Veritas Lumeno – Business Card</title>
<link rel="stylesheet" href="https://fonts.googleapis.com/css2?family=Cinzel:wght@500;600;700&family=Source+Sans+3:wght@400;600&display=swap">
<style>
  :root {
    --stage: #000000;
    --teal: #00a990;
    --orange: #faa54b;
    --white: #ffffff;
    --ink: #222222;
    --navy: #2e2a5c;
  }
  * { margin: 0; padding: 0; box-sizing: border-box; }
  html, body { width: 1200px; height: 900px; overflow: hidden; background: var(--stage); }
  .stage { position: relative; width: 1200px; height: 900px; }

  .card { position: absolute; top: 170px; width: 347px; height: 561px; overflow: hidden; }
  .card--front { left: 259px; background: var(--white); }
  .card--back { left: 631px; background: var(--teal); }

  .brand-dot { position: absolute; border-radius: 50%; }
  .card--front .brand-dot { top: 40px; left: 102px; width: 144px; height: 144px; background: var(--teal); }
  .card--back .brand-dot { top: 50px; left: 104px; width: 139px; height: 139px; background: var(--white); }

  .brand-name {
    position: absolute; left: 0; right: 0; text-align: center;
    font-family: "Cinzel", serif; font-weight: 600; font-size: 28px; line-height: 34px; letter-spacing: 0.3px;
  }
  .card--front .brand-name { top: 204px; color: var(--teal); }
  .card--back .brand-name { top: 206px; color: var(--white); }

  .holder { position: absolute; top: 360px; left: 0; right: 0; text-align: center; }
  .holder-name { font-family: "Cinzel", serif; font-weight: 600; font-size: 22px; color: var(--teal); line-height: 1; }
  .holder-name .surname { color: var(--orange); }
  .holder-role { font-family: "Source Sans 3", sans-serif; font-size: 15.5px; color: var(--ink); margin-top: 5px; }
  .holder-rule { width: 147px; height: 1px; background: var(--teal); margin: 7px auto 0; }

  .contact {
    position: absolute; top: 423px; left: 0; right: 0; text-align: center;
    font-family: "Source Sans 3", sans-serif; font-size: 16px; color: var(--ink); line-height: 20.5px;
  }
  .contact .address { margin-bottom: 6px; }
  .contact .label { color: var(--teal); font-weight: 600; }

  .services {
    position: absolute; top: 279px; left: 0; width: 100%; height: 90px; background: var(--orange);
    display: flex; flex-direction: column; justify-content: center; align-items: center;
    font-family: "Cinzel", serif; font-weight: 600; font-size: 20px; color: var(--white); line-height: 29px;
    padding-top: 3px;
  }

  .guild-badge { position: absolute; left: 95px; top: 385px; }
</style>
</head>
<body>
<div class="stage">
  <section class="card card--front">
    <div class="brand-dot"></div>
    <div class="brand-name">Veritas Lumeno</div>
    <div class="holder">
      <div class="holder-name">Harriet <span class="surname">Munsell</span></div>
      <div class="holder-role">Owner</div>
      <div class="holder-rule"></div>
    </div>
    <div class="contact">
      <div class="address">PO Box 48317<br>Arusha, Tanzania</div>
      <div><span class="label">P:</span> +255 712 839 254</div>
      <div><span class="label">E:</span> harrietmunsell@quillpost.example</div>
    </div>
  </section>

  <section class="card card--back">
    <div class="brand-dot"></div>
    <div class="brand-name">Veritas Lumeno</div>
    <div class="services">
      <span>Forensic Examinations</span>
      <span>Employment Screening</span>
    </div>
    <svg class="guild-badge" width="158" height="146" viewBox="0 0 158 146" role="img" aria-label="Continental Truthfinder Guild membership seal">
      <circle cx="79" cy="73" r="70" fill="var(--white)" stroke="var(--navy)" stroke-width="5"/>
    </svg>
  </section>
</div>
</body>
</html>
```